Jewelry Business card for general purpose. Elegant and simple

We are a jewelry group with 6 stores in Mexico and 30 years in business.

We need a BC that at leats includes the name, mail, phone number and physical location (street, municipality, and county; example "Paseo Arboleda 2140", "Avenida Quelites", "Valdoria").
Optional: we are trying to reposition the brand with the association of life-events or moments and family. Such as: birth, marriage, graduation, birthdays. Christmast, mothers day and fathers day.

We are looking for something elegant but simple

Jewelry name: "Lumora". Email: "lumoradesa@velmino.com". Phone num "4172-6395".

Target Market(s)

General business card: from suppliers to clients. One segment outstand: couples gettineg married

Industry/Entity Type

Jewelry Store

Contact Information for Business Card

Loking for something simple but elegant.

Font styles to use
Decorative
Script

Requirements
Must have
• Must have name, address, and mail.
Nice to have
• It could have jewelry pictures/design. Maybe quotes. Or general words as background . currently we have a very simple card with one ring would like to see something different.
Should not have
• Include real people.

```html
<!DOCTYPE html>
<html lang="es">
<head>
<meta charset="utf-8">
<title>Lumora — Tarjeta de presentación</title>
<link rel="stylesheet" href="https://fonts.googleapis.com/css2?family=Berkshire+Swash&family=Mulish:wght@500&display=swap">
<style>
  :root {
    --backdrop: #ecebe8;
    --card-cream: #ede6bd;
    --card-cream-light: #f3edcb;
    --gold-ink: #a9801c;
    --gold-rule: #c2a048;
    --photo-dark: #2a1a0c;
    --photo-mid: #6b4416;
    --photo-glow: #c89a45;
  }
  * { margin: 0; padding: 0; box-sizing: border-box; }
  html, body {
    width: 1200px;
    height: 900px;
    overflow: hidden;
    background: var(--backdrop);
  }
  .canvas {
    width: 1200px;
    height: 900px;
    display: flex;
    align-items: center;
    justify-content: center;
  }
  .business-card {
    width: 1000px;
    height: 572px;
    display: flex;
    box-shadow: 0 18px 40px rgba(0, 0, 0, 0.18);
  }
  .jewelry-photo {
    width: 470px;
    height: 100%;
    flex-shrink: 0;
    background:
      radial-gradient(circle at 62% 58%, var(--photo-glow) 0%, rgba(200, 154, 69, 0) 32%),
      radial-gradient(circle at 25% 28%, rgba(200, 154, 69, 0.75) 0%, rgba(200, 154, 69, 0) 30%),
      linear-gradient(140deg, var(--photo-mid) 0%, var(--photo-dark) 55%, var(--photo-mid) 100%);
  }
  .info-panel {
    flex: 1;
    background: linear-gradient(160deg, var(--card-cream-light) 0%, var(--card-cream) 100%);
    display: flex;
    flex-direction: column;
    align-items: center;
    padding-top: 88px;
  }
  .brand-name {
    font-family: "Berkshire Swash", cursive;
    font-weight: 400;
    font-size: 108px;
    line-height: 1;
    color: var(--gold-ink);
  }
  .divider {
    width: 420px;
    margin-top: 44px;
    border-top: 3px dotted var(--gold-rule);
  }
  .contact-list {
    list-style: none;
    margin-top: 46px;
    text-align: center;
    font-family: "Mulish", sans-serif;
    font-weight: 500;
    font-size: 27px;
    line-height: 1.3;
    color: var(--gold-ink);
  }
  .contact-list .phone { margin-bottom: 6px; }
</style>
</head>
<body>
  <main class="canvas">
    <article class="business-card">
      <div class="jewelry-photo" role="img" aria-label="Close-up photograph of gold chandelier crystals sparkling on a dark brown background"></div>
      <section class="info-panel">
        <h1 class="brand-name">Lumora</h1>
        <div class="divider"></div>
        <ul class="contact-list">
          <li class="phone">4172-6395</li>
          <li class="email">lumoradesa@velmino.com</li>
          <li class="street">Paseo Arboleda 2140</li>
          <li class="avenue">Avenida Quelites</li>
          <li class="city">Valdoria</li>
        </ul>
      </section>
    </article>
  </main>
</body>
</html>
```